Funeral Services Site

We need a website for a Funeral Services company. The old website is: www.rouwcentrumkorvelaer.be We need the same structure and text.

Target Market(s)

Customers.

Coding

Coded - Design and coding required

Number of Pages Required

4 page

Font styles to use
Serif
Sans Serif
Script

```html
<!DOCTYPE html>
<html lang="en">
<head>
<meta charset="utf-8">
<title>Funeral Home Korvelaer BVBA</title>
<link rel="stylesheet" href="https://fonts.googleapis.com/css2?family=Roboto+Slab:wght@400;700&family=Lora:ital@1&family=Open+Sans:wght@400;600;700&display=swap">
<style>
:root{
  --ink:#2b2b2b;
  --dark:#1d1d1d;
  --mid:#3a3a3a;
  --text:#666;
  --muted:#999;
  --line:#d8d8d8;
  --light:#f2f2f2;
  --white:#fff;
  --accent:#4a4a4a;
}
*{box-sizing:border-box;margin:0;padding:0}
html,body{width:1200px;height:3988px;overflow:hidden;background:var(--white)}
body{font-family:"Open Sans",Arial,sans-serif;color:var(--text);font-size:14px;position:relative}
section,header,footer{position:absolute;left:0;width:1200px}

/* header */
.site-header{top:0;height:92px;background:var(--white);z-index:3;box-shadow:0 2px 6px rgba(0,0,0,.12)}
.brand{position:absolute;left:116px;top:14px;display:flex;align-items:center;gap:12px}
.brand-mark{width:48px;height:48px;border-radius:50%;background:var(--ink)}
.brand-name{font-family:"Roboto Slab",Georgia,serif;font-size:22px;line-height:24px;color:var(--ink);font-weight:700}
.top-tools{position:absolute;right:116px;top:10px;display:flex;gap:8px;align-items:center}
.pill{background:var(--ink);color:#fff;font-size:11px;font-weight:700;padding:5px 12px;border-radius:3px}
.lang{width:20px;height:13px;background:#bbb;border-radius:2px}
.nav{position:absolute;right:110px;top:50px;display:flex;gap:6px}
.nav a{font-size:12px;color:var(--ink);text-decoration:none;padding:6px 14px;border:1px solid transparent}
.nav a.active{border-color:var(--ink);border-radius:3px}

/* hero */
.hero{top:0;height:690px}
.hero-photo{position:absolute;inset:0;background:linear-gradient(180deg,#4a4b3c 0%,#6d6a55 35%,#3c3a30 70%,#25241f 100%)}
.hero-copy{position:absolute;top:355px;width:100%;text-align:center;color:#fff}
.hero-copy h1{font-family:"Roboto Slab",Georgia,serif;font-weight:400;font-size:50px;letter-spacing:3px}
.hero-copy p{font-family:"Roboto Slab",Georgia,serif;font-size:22px;letter-spacing:3px;margin-top:10px}
.hero-actions{margin-top:40px;display:flex;justify-content:center;gap:14px}
.btn-ghost{border:2px solid #fff;color:#fff;font-size:15px;padding:10px 22px;border-radius:4px;background:rgba(0,0,0,.35)}
.hero-curve{position:absolute;bottom:0;left:0}

/* intro */
.intro{top:690px;height:500px;text-align:center}
.intro h2{font-family:"Lora",Georgia,serif;font-style:italic;font-weight:400;font-size:32px;color:#555;line-height:44px;margin-top:95px}
.rule-title{display:flex;align-items:center;justify-content:center;gap:18px;margin-top:30px;font-family:"Roboto Slab",Georgia,serif;font-size:24px;color:var(--ink);letter-spacing:2px}
.rule-title::before,.rule-title::after{content:"";width:90px;height:1px;background:var(--ink)}
.intro p{width:960px;margin:24px auto 0;font-size:13px;line-height:22px;color:var(--text)}
.btn-outline{display:inline-block;margin-top:30px;border:1px solid var(--ink);border-radius:14px;padding:5px 22px;font-size:11px;color:var(--ink);font-weight:600}

/* organization */
.organization{top:1190px;height:520px;color:#ddd}
.org-photo{position:absolute;inset:0;background:linear-gradient(90deg,#121212 0%,#2d2a26 40%,#4b4337 70%,#1b1a18 100%)}
.organization h2{position:absolute;top:100px;width:100%;text-align:center;font-family:"Roboto Slab",Georgia,serif;font-size:26px;color:#fff;font-weight:400;letter-spacing:1px}
.org-text{position:absolute;left:120px;top:160px;width:470px;font-size:13px;line-height:22px}
.org-list{position:absolute;left:680px;top:160px;width:420px;list-style:none}
.org-list li{display:flex;gap:12px;font-size:13px;line-height:20px;margin-bottom:22px;color:#fff}
.org-list svg{flex:none;margin-top:3px}

/* gallery */
.gallery{top:1700px;height:760px;text-align:center}
.gallery h2{margin-top:45px;font-family:"Roboto Slab",Georgia,serif;font-size:26px;color:var(--ink);font-weight:700;letter-spacing:1px}
.grid{display:grid;grid-template-columns:repeat(4,240px);grid-auto-rows:232px;gap:8px;justify-content:center;margin-top:40px}
.tile{border-radius:2px}
.t1{background:radial-gradient(circle,#f4f4ee,#9aa58c)}
.t2{background:radial-gradient(circle,#e9b7c9,#f2f2f2)}
.t3{background:radial-gradient(circle,#e58f6a,#c9b28a)}
.t4{background:radial-gradient(circle,#f1f1ea,#b9c2a8)}
.t5{background:radial-gradient(circle,#fbfbf6,#a7b494)}
.t6{background:radial-gradient(circle,#e0b131,#5a2a16)}
.t7{background:radial-gradient(circle,#e6cc3c,#35472a)}
.t8{background:radial-gradient(circle,#f0efe8,#6f8a57)}
.gallery .btn-outline{margin-top:38px}

/* contact band */
.contact-band{top:2470px;height:300px;background:linear-gradient(90deg,#e8e8e8,#f6f6f6 60%,#e4e4e4)}
.contact-band h3{position:absolute;left:140px;top:84px;width:440px;font-family:"Roboto Slab",Georgia,serif;font-size:17px;line-height:26px;color:var(--ink);letter-spacing:1.5px;font-weight:700}
.band-actions{position:absolute;left:140px;top:196px;display:flex;gap:10px}
.btn-dark{background:var(--ink);color:#fff;font-size:12px;padding:6px 16px;border-radius:14px;display:flex;align-items:center;gap:6px}
.band-flowers{position:absolute;left:700px;top:40px;width:320px;height:230px;border-radius:50%;background:radial-gradient(ellipse,#f7f7f2 20%,#a9b59a 55%,rgba(230,230,230,0) 72%)}

/* condole */
.condole{top:2770px;height:700px;text-align:center}
.condole h2{margin-top:115px;font-family:"Roboto Slab",Georgia,serif;font-size:28px;color:var(--ink);letter-spacing:1px}
.condole .lead{width:900px;margin:28px auto 0;font-size:12px;line-height:20px;color:var(--text)}
.people{position:absolute;top:250px;left:100px;width:1000px;display:flex;justify-content:space-between;align-items:flex-start}
.person{width:230px;padding:16px 0 20px;text-align:center}
.person.featured{background:var(--white);box-shadow:0 0 10px rgba(0,0,0,.18)}
.portrait{width:180px;height:180px;border-radius:50%;margin:0 auto;border:5px solid #e9e9e9;background:radial-gradient(circle at 50% 40%,#c9c3ba,#7c776f)}
.person h4{font-family:"Roboto Slab",Georgia,serif;font-size:16px;color:var(--ink);margin-top:16px;font-weight:400;line-height:20px}
.person .dates{font-size:11px;color:var(--muted);margin-top:6px}
.small-btn{display:block;width:150px;margin:10px auto 0;background:var(--mid);color:#fff;font-size:10px;padding:4px 0}

/* footer */
.site-footer{top:3440px;height:548px}
.footer-curve{position:absolute;top:0;left:0}
.footer-body{position:absolute;top:60px;left:0;width:1200px;height:448px;background:var(--dark)}
.footer-mark{position:absolute;left:578px;top:22px;width:44px;height:44px;border-radius:50%;background:var(--white)}
.footer-col{position:absolute;top:100px;color:#ccc}
.footer-col h3{font-family:"Roboto Slab",Georgia,serif;color:#fff;font-size:20px;font-weight:400;margin-bottom:24px}
.form{left:120px;width:520px}
.form .row{display:flex;gap:10px;margin-bottom:10px}
.field{background:#fff;height:30px;flex:1;font-size:11px;color:#999;padding:7px 8px}
.field.area{height:90px}
.submit{float:right;background:#fff;color:var(--ink);font-size:11px;font-weight:700;padding:5px 14px;border-radius:3px}
.info{left:730px;width:360px;font-size:12px}
.info p{display:flex;gap:10px;align-items:center;margin-bottom:12px}
.icon-dot{width:14px;height:14px;border-radius:50%;background:#777;flex:none}
.social{display:flex;gap:8px;margin-top:16px}
.social span{width:22px;height:22px;border-radius:50%;background:#666}
.footer-links{position:absolute;right:120px;bottom:66px;font-size:11px;color:#aaa}
.copy-bar{position:absolute;bottom:0;left:0;width:1200px;height:40px;background:#111;font-size:11px;color:#999;padding:12px 120px}
</style>
</head>
<body>

<section class="hero">
  <div class="hero-photo" role="img" aria-label="Photograph of a wooden coffin decorated with white and green flowers"></div>
  <div class="hero-copy">
    <h1>FUNERAL HOME KORVELAER BVBA</h1>
    <p>A PERSONAL SERVICE IN FAREWELL GUIDANCE</p>
    <div class="hero-actions">
      <span class="btn-ghost">012 48 70 36</span>
      <span class="btn-ghost">CONTACT US</span>
    </div>
  </div>
  <svg class="hero-curve" width="1200" height="70" viewBox="0 0 1200 70">
    <path d="M0 70 L0 40 Q600 -10 1200 40 L1200 70 Z" fill="#fff"/>
    <circle cx="582" cy="22" r="13" fill="#fff" stroke="#444"/>
    <circle cx="618" cy="22" r="13" fill="#fff" stroke="#444"/>
    <path d="M585 16 L579 22 L585 28" stroke="#333" stroke-width="2" fill="none"/>
    <path d="M615 16 L621 22 L615 28" stroke="#333" stroke-width="2" fill="none"/>
  </svg>
</section>

<header class="site-header">
  <div class="brand"><span class="brand-mark"></span><span class="brand-name">Funeral home<br>Korvelaer</span></div>
  <div class="top-tools">
    <span class="pill">012 48 70 36</span>
    <span class="pill">SEND E-MAIL</span>
    <span class="lang"></span><span class="lang"></span>
  </div>
  <nav class="nav">
    <a class="active">Home</a><a>About us</a><a>Condole online</a><a>Order flowers</a><a>Contact us</a>
  </nav>
</header>

<section class="intro">
  <h2>Mourning center Korvelaer, a complete service in mourning<br>and farewell guidance</h2>
  <div class="rule-title">ABOUT US</div>
  <p>Saying goodbye to a loved one is one of the toughest things in a lifetime. Funeral home Korvelaer in our town takes care of <strong>all the practical and administrative matters</strong> involved, so you can say goodbye in peace.</p>
  <p style="margin-top:12px">Our people have <strong>years of experience in farewell guidance</strong> and stand by you 24 hours a day. Our fully renovated funeral home is open to you and your loved ones, so that you can grieve in a familiar place at any time.</p>
  <span class="btn-outline">READ MORE ›</span>
</section>

<section class="organization">
  <div class="org-photo" role="img" aria-label="Dark photograph of burning candles in a chapel"></div>
  <h2>ORGANIZATION FUNERAL AND WORSHIP</h2>
  <p class="org-text">The organization of the funeral ceremony is a moment of reflection, where the personality of the deceased can be beautifully highlighted. Our team will assist you in this and select <strong>the most beautiful texts, songs and photos</strong> with you in order to arrive at an appropriate and worthy goodbye.<br><br>The funeral can take place in your parish church or our auditorium if you wish, which can accommodate a maximum of 150 guests. We also arrange the following for you.</p>
  <ul class="org-list">
    <li><svg width="14" height="14" viewBox="0 0 14 14"><path d="M2 7 L6 11 L12 3" stroke="#fff" stroke-width="2" fill="none"/></svg>Vigil the night before the funeral</li>
    <li><svg width="14" height="14" viewBox="0 0 14 14"><path d="M2 7 L6 11 L12 3" stroke="#fff" stroke-width="2" fill="none"/></svg>Prayer service with priest (if possible)</li>
    <li><svg width="14" height="14" viewBox="0 0 14 14"><path d="M2 7 L6 11 L12 3" stroke="#fff" stroke-width="2" fill="none"/></svg>Eucharistic celebration with priest on Tuesday and Friday in the parishes of the town</li>
  </ul>
  <svg style="position:absolute;bottom:0;left:0" width="1200" height="50" viewBox="0 0 1200 50"><path d="M0 50 L0 30 Q600 -10 1200 30 L1200 50 Z" fill="#fff"/></svg>
</section>

<section class="gallery">
  <h2>PHOTO GALLERY</h2>
  <div class="grid">
    <div class="tile t1" role="img" aria-label="White heart-shaped flower wreath"></div>
    <div class="tile t2" role="img" aria-label="Pink and white cross-shaped flower arrangement"></div>
    <div class="tile t3" role="img" aria-label="Round arrangement of orange and pink roses"></div>
    <div class="tile t4" role="img" aria-label="White floral wreath with greenery"></div>
    <div class="tile t5" role="img" aria-label="White roses funeral arrangement"></div>
    <div class="tile t6" role="img" aria-label="Yellow and orange round flower arrangement"></div>
    <div class="tile t7" role="img" aria-label="Yellow and white floral wreath"></div>
    <div class="tile t8" role="img" aria-label="White flower wreath with green leaves"></div>
  </div>
  <span class="btn-outline">VIEW ALL ›</span>
</section>

<section class="contact-band">
  <h3>DO YOU HAVE ANY QUESTIONS OR WOULD YOU LIKE TO CALL IN OUR FUNERAL HOME? CONTACT US. WE ARE HERE FOR YOU.</h3>
  <div class="band-actions">
    <span class="btn-dark"><svg width="11" height="11" viewBox="0 0 12 12"><path d="M2 1 L4.5 1 L5.5 4 L4 5 Q5 7.5 7 8 L8 6.5 L11 7.5 L11 10 Q6 12 2 6 Q1 3 2 1Z" fill="#fff"/></svg>012 48 70 36</span>
    <span class="btn-dark">CONTACT US</span>
  </div>
  <div class="band-flowers" role="img" aria-label="White flower arrangement with green leaves"></div>
</section>

<section class="condole">
  <h2>CONDOLE ONLINE</h2>
  <p class="lead">Do you want to show your sympathy to the family of a deceased one? Funeral home Korvelaer gives you the opportunity to convey your message quickly and discreetly. Here you can condole the family of a recently deceased person online.</p>
  <div class="people">
    <div class="person"><div class="portrait" role="img" aria-label="Portrait photo of the deceased"></div><h4>Greta<br>Vermeulen</h4><p class="dates">June 14, 1941 - May 3, 2020</p></div>
    <div class="person featured"><div class="portrait" role="img" aria-label="Portrait photo of the deceased"></div><h4>Willy August<br>Jansens</h4><p class="dates">Feb 11, 1937 - May 1, 2020</p><span class="small-btn">Download funeral letter</span><span class="small-btn">Order flowers</span></div>
    <div class="person"><div class="portrait" role="img" aria-label="Portrait photo of the deceased"></div><h4>Rosa<br>Claes</h4><p class="dates">Aug 30, 1934 - April 27, 2020</p></div>
    <div class="person"><div class="portrait" role="img" aria-label="Portrait photo of the deceased"></div><h4>Denise<br>Wouters</h4><p class="dates">Nov 2, 1938 - April 24, 2020</p></div>
  </div>
</section>

<footer class="site-footer">
  <svg class="footer-curve" width="1200" height="62" viewBox="0 0 1200 62"><path d="M0 62 L0 40 Q600 0 1200 40 L1200 62 Z" fill="#1d1d1d"/></svg>
  <div class="footer-mark"></div>
  <div class="footer-body">
    <div class="footer-col form">
      <h3>Get In Touch</h3>
      <div class="row"><span class="field">Name</span><span class="field">Phone</span></div>
      <div class="row"><span class="field">Mail</span></div>
      <div class="row"><span class="field area">Comment</span></div>
      <span class="submit">SUBMIT</span>
    </div>
    <div class="footer-col info">
      <h3>Contact information</h3>
      <p><span class="icon-dot"></span>012 48 70 36</p>
      <p><span class="icon-dot"></span>info@rouwcentrumkorvelaer.be</p>
      <p><span class="icon-dot"></span>Kerkstraat 12, 3700 Tongeren (Belgium)</p>
      <div class="social"><span></span><span></span><span></span><span></span><span></span></div>
    </div>
    <div class="footer-links">Sitemap &nbsp;|&nbsp; Privacy Policy</div>
  </div>
  <div class="copy-bar">Copyright © 2020 Funeral Home Korvelaer. All Rights Reserved.</div>
</footer>

</body>
</html>
```